Veltarum

Standard Business Card design.
Sample two-sided design uploaded. White front, Black back.
Would like white shield to be on all black background side.
Willing to look at a couple creative designs, but nothing crazy.
Preference for a classic, confident, strong design.

```html
<!DOCTYPE html>
<html lang="en">
<head>
<meta charset="UTF-8">
<title>Veltarum — Business Card</title>
<link rel="stylesheet" href="https://fonts.googleapis.com/css2?family=Roboto+Condensed:wght@700&family=Inter:wght@400;600&display=swap">
<style>
  :root {
    --backdrop: #e3e2e0;
    --paper: #f7f7f6;
    --ink: #111111;
    --card-black: #1b1b1b;
    --white: #f4f4f2;
  }
  * { margin: 0; padding: 0; box-sizing: border-box; }
  html, body {
    width: 1200px; height: 1200px; overflow: hidden;
    background: var(--backdrop);
  }
  .sheet {
    width: 1200px; height: 1200px;
    display: flex; flex-direction: column; align-items: center; justify-content: center;
    gap: 44px;
  }
  .card {
    position: relative;
    width: 900px; height: 514px;
    box-shadow: 0 2px 6px rgba(0,0,0,0.12);
    overflow: hidden;
  }
  .card--front { background: var(--paper); color: var(--ink); }
  .card--back { background: var(--card-black); }

  .square-row { position: absolute; display: flex; gap: 9px; }
  .square-row span { display: block; width: 30px; height: 30px; background: var(--ink); }
  .square-row--top { top: 6px; left: 0; }
  .square-row--bottom { bottom: 36px; right: 0; }

  .brand {
    position: absolute; top: 58px; right: 94px;
    display: flex; align-items: center; gap: 12px;
    font-family: "Inter", sans-serif; font-weight: 600;
    font-size: 26px; letter-spacing: 3px; color: var(--ink);
  }
  .brand__mark { width: 14px; height: 14px; background: var(--ink); }

  .person { position: absolute; left: 58px; top: 344px; }
  .person__name {
    font-family: "Roboto Condensed", sans-serif; font-weight: 700;
    font-size: 32px; line-height: 1.1;
  }
  .person__role {
    font-family: "Inter", sans-serif; font-weight: 400;
    font-size: 18px; margin-top: 8px; margin-left: 4px;
  }
  .contact {
    position: absolute; left: 62px; top: 432px;
    font-family: "Inter", sans-serif; font-size: 18px; line-height: 1.3;
    list-style: none;
  }

  .back-name {
    position: absolute; inset: 0;
    display: flex; align-items: center; justify-content: center; gap: 18px;
    font-family: "Inter", sans-serif; font-weight: 600;
    font-size: 46px; letter-spacing: 6px; color: var(--white);
  }
  .back-name__mark { width: 22px; height: 22px; background: var(--white); }
</style>
</head>
<body>
<main class="sheet">
  <section class="card card--front" aria-label="Card front">
    <div class="square-row square-row--top"><span></span><span></span><span></span><span></span><span></span></div>
    <div class="brand"><span class="brand__mark"></span>VELTARUM</div>
    <div class="person">
      <h1 class="person__name">Mara Lindqvist</h1>
      <p class="person__role">Exicutive Director</p>
    </div>
    <ul class="contact">
      <li>hello@youremail.com</li>
      <li>www.yourwebsite.com</li>
      <li>123-456-7896</li>
    </ul>
    <div class="square-row square-row--bottom"><span></span><span></span><span></span><span></span><span></span></div>
  </section>

  <section class="card card--back" aria-label="Card back">
    <div class="back-name"><span class="back-name__mark"></span>VELTARUM</div>
  </section>
</main>
</body>
</html>
```